Duel Business card

Want an edgy business card that shows both of our companies on each side of the card, OR both together with a cool design.

*Must be edgy: We have attached our two business logos. We are a bail bond and immigration bond company.

Would like the address on one side only.
Need Phone, cell, website, address, and Name

Company Name 1: Cellgate Release Partners
www.cellgatereleasepartners.example

Company Name 2: Borderline Surety Associates
www.borderlinesuretyassociates.example

These cards will need to be easily changeable so I can modify new employees

Target Market(s)

people in jail, takign imigrants out of jail and from being taken back to there country

Industry/Entity Type

Business

Requirements
Must have
• Include both logos attached

```html
<!DOCTYPE html>
<html lang="en">
<head>
<meta charset="UTF-8">
<title>Dual Business Card – Cellgate Release Partners &amp; Borderline Surety Associates</title>
<link href="https://fonts.googleapis.com/css2?family=Questrial&display=swap" rel="stylesheet">
<style>
  :root {
    --stage: #1c1c1c;
    --card-black: #0d0d0d;
    --card-back: #2f2f2f;
    --card-back-light: #3d3d3d;
    --accent-yellow: #ecc817;
    --accent-red: #e0282a;
    --brand-blue: #2b2a85;
    --text-white: #f2f2f2;
    --text-muted: #8a8a8a;
    --ring-grey: #cfcfcf;
  }
  * { margin: 0; padding: 0; box-sizing: border-box; }
  html, body {
    width: 1200px; height: 900px; overflow: hidden;
    background: var(--stage);
    font-family: "Questrial", "Century Gothic", sans-serif;
  }
  .canvas { position: relative; width: 1200px; height: 900px; }

  .card {
    position: absolute;
    width: 640px; height: 380px;
    box-shadow: 0 18px 40px rgba(0,0,0,.6);
    overflow: hidden;
  }

  /* Front */
  .card-front { left: 90px; top: 60px; background: var(--card-black); }
  .stripe { position: absolute; height: 11px; background: var(--accent-yellow); }
  .stripe-top { top: 0; left: 160px; right: 0; }
  .stripe-bottom { bottom: 0; left: 0; right: 150px; }
  .squares { position: absolute; display: flex; gap: 10px; }
  .squares span { width: 22px; height: 14px; background: var(--accent-red); }
  .squares-top { top: 26px; left: 18px; }
  .squares-bottom { bottom: 26px; right: 18px; }

  .brand { position: absolute; display: flex; flex-direction: column; align-items: center; text-align: center; }
  .brand-mark { width: 110px; height: 110px; border-radius: 50%; margin-bottom: 18px; }
  .brand-name { font-size: 26px; line-height: 1.15; letter-spacing: .5px; }

  .brand-surety { left: 40px; top: 92px; width: 230px; }
  .brand-surety .brand-mark { border: 4px solid var(--ring-grey); }
  .brand-surety .brand-name { color: var(--accent-red); }

  .brand-cellgate { left: 320px; top: 92px; width: 290px; }
  .brand-cellgate .brand-mark { background: var(--brand-blue); }
  .brand-cellgate .brand-name { color: var(--accent-yellow); font-size: 30px; }

  /* Back */
  .card-back {
    left: 470px; top: 470px;
    background: radial-gradient(circle at 88% 10%, var(--card-back-light) 0%, var(--card-back) 55%, #262626 100%);
    padding: 44px 48px;
  }
  .person-name { color: var(--accent-red); font-size: 19px; text-transform: uppercase; letter-spacing: .5px; }
  .person-role { color: var(--accent-red); font-size: 15px; margin-bottom: 26px; }
  .contact-list { list-style: none; margin-bottom: 24px; }
  .contact-list li { color: var(--text-white); font-size: 16px; line-height: 1.3; }
  .contact-list .label { color: var(--accent-red); }
  .company { color: var(--text-muted); font-size: 15px; line-height: 1.3; margin-bottom: 14px; }
</style>
</head>
<body>
<main class="canvas">

  <section class="card card-front" aria-label="Card front">
    <div class="stripe stripe-top"></div>
    <div class="squares squares-top"><span></span><span></span><span></span><span></span></div>

    <div class="brand brand-surety">
      <div class="brand-mark"></div>
      <p class="brand-name">Borderline Surety Associates</p>
    </div>

    <div class="brand brand-cellgate">
      <div class="brand-mark"></div>
      <p class="brand-name">Cellgate Release Partners</p>
    </div>

    <div class="squares squares-bottom"><span></span><span></span><span></span><span></span></div>
    <div class="stripe stripe-bottom"></div>
  </section>

  <section class="card card-back" aria-label="Card back">
    <p class="person-name">Dana Whitfield</p>
    <p class="person-role">Managing Director</p>
    <ul class="contact-list">
      <li><span class="label">Phone:</span> 555 014 2270</li>
      <li><span class="label">Mobile:</span> 555 018 3391</li>
      <li><span class="label">Website:</span> www.releasepartnersgroup.example</li>
      <li><span class="label">Address:</span> 410 Harrow Lane Fairbridge CA</li>
    </ul>
    <p class="company">Cellgate Release Partners<br>www.cellgatereleasepartners.example</p>
    <p class="company">Borderline Surety Associates<br>www.borderlinesuretyassociates.example</p>
  </section>

</main>
</body>
</html>
```